Flyer - Crestline Dental Marbury

** Please do not use my words - word-for-word on the flyer design **
We have recently bought an established dental business. However we are not getting new customers through the door. We plan to implement aggressive local marketing strategies including flyer distribution. We are looking for an eye-catching must read flyer design. Some details & content ideas are as below.
1. A5 size - Double Sided
2. Our business name is Crestline Dental Marbury. Logo is attached. Website is www.crestlinedentalmarbury.com.au where lot of useful information can be found.
3. Practice has a long & proud history serving "Lower North Shore" since 1958. We provide quality dental care at affordable prices.
4. List of services can be found on website
5. Perhaps a snippet of Orbisa Map Location would be useful. Also the fact that 3-hour free parking is available in Fernleigh Arcade less than 100m away from practice. Plenty of 2-hours street parking is available too.
6. Opening hours can be found on website. Fact that we are open on Saturdays and till late on Tuesdays is worth calling out.
7. We would like to run a campaign of offers with this flyer. Give it a name! Details below.
a) NO GAP Checkup and Clean with any major Private Health Fund. Includes oral exam, 2 X-Rays, Scale & Polish and Fluoride Treatment
b) Genuine Teeth Whitening for $199 (usually $399 save $200)
c) 10% off on all major dental. Includes fillings, crowns, bridges and root canal treatment
8. We are KELMA Preferred Provider means KELMA members get maximum benefit. KELMA Patron Plus logo attached.
9. We participate in Office of Ranger Welfare Fee Schedule. Logo attached.
10. Call out WE ACCEPT ALL HEALTH FUNDS
Dental
- Helvetica Neue, Myriad Pro

```html
<!DOCTYPE html>
<html lang="en">
<head>
<meta charset="utf-8">
<title>Crestline Dental Marbury – Flyer</title>
<link rel="stylesheet" href="https://fonts.googleapis.com/css2?family=Oswald:wght@500;600&family=Roboto:wght@300;400;500;700;900&display=swap">
<style>
  :root{
    --teal:#5fc39b;
    --teal-dark:#3fa97f;
    --lime:#8dc63f;
    --lime-dark:#6fae2c;
    --lime-soft:#a9d356;
    --white:#ffffff;
    --photo-a:#f4f4f2;
    --photo-b:#e2dcd2;
  }
  *{box-sizing:border-box;margin:0;padding:0}
  html,body{width:985px;height:1200px;overflow:hidden;background:#eef1ee}
  .flyer{position:relative;width:985px;height:1200px;background:var(--white);overflow:hidden;font-family:"Roboto",Helvetica,Arial,sans-serif}

  .brand{position:absolute;left:46px;top:92px;display:flex;align-items:center;gap:14px}
  .brand-dot{width:58px;height:58px;border-radius:50%;background:var(--teal)}
  .brand-name{font-weight:500;font-size:30px;line-height:1.1;color:var(--teal)}

  .ribbon{position:absolute;left:0;top:0;width:985px;height:300px}
  .ribbon-text{position:absolute;left:410px;top:86px;width:555px;font-family:"Oswald",sans-serif;font-weight:600;color:var(--white);font-size:46px;line-height:54px;text-align:center;letter-spacing:1px}
  .ribbon-care{position:absolute;left:555px;top:200px;width:390px;height:76px;background:var(--lime-soft);color:var(--white);font-family:"Oswald",sans-serif;font-weight:600;font-size:50px;line-height:76px;text-align:center;letter-spacing:2px}

  .photo{position:absolute;left:0;top:290px;width:985px;height:430px;background:linear-gradient(160deg,var(--photo-a) 0%,#ece8e1 55%,var(--photo-b) 100%)}

  .web-band{position:absolute;right:0;top:694px;width:470px;height:44px;background:var(--teal);color:var(--white);font-size:21px;line-height:44px;padding-left:22px}

  .slogan-band{position:absolute;left:0;top:738px;width:985px;height:142px;background:var(--teal);padding:18px 0 0 58px;color:var(--white);font-weight:300;font-size:48px;line-height:56px}
  .slogan-band .strong{font-weight:400}

  .hours{position:absolute;left:70px;top:900px;width:440px}
  .hours-title{background:var(--lime);color:var(--white);font-weight:900;font-size:28px;text-align:center;height:40px;line-height:40px;margin-bottom:3px}
  .hours-row{display:grid;grid-template-columns:200px 1fr;gap:3px;margin-bottom:3px;height:30px}
  .hours-day{background:var(--lime);color:var(--white);font-weight:700;font-size:23px;line-height:30px;padding-left:12px}
  .hours-day.small{font-size:15px}
  .hours-time{background:var(--lime-dark);color:var(--white);font-size:22px;line-height:30px;text-align:center}

  .funds{position:absolute;left:538px;top:912px;color:var(--teal);font-size:23px;line-height:27px;text-transform:uppercase}

  .badge{position:absolute;left:760px;top:822px;width:210px;height:210px}
  .badge-text{position:absolute;left:0;top:0;width:210px;height:210px;text-align:center;color:var(--lime)}
  .badge-stars{position:absolute;left:0;width:210px;font-size:14px;letter-spacing:6px}
  .badge-pct{position:absolute;top:60px;left:0;width:210px;font-weight:700;font-size:58px;line-height:58px}
  .badge-off{position:absolute;top:118px;left:0;width:210px;font-weight:700;font-size:40px;line-height:40px}

  .offer-strip{position:absolute;right:0;top:1042px;width:445px;height:46px;background:var(--lime-soft);color:var(--white);font-weight:500;font-size:15px;line-height:20px;text-align:center;padding-top:3px}

  .call-band{position:absolute;left:0;top:1100px;width:985px;height:100px;background:var(--teal);color:var(--white);font-weight:900;font-size:76px;line-height:100px;padding-left:44px;letter-spacing:1px}
</style>
</head>
<body>
<main class="flyer">

  <div class="brand">
    <span class="brand-dot"></span>
    <span class="brand-name">Crestline Dental<br>Marbury</span>
  </div>

  <svg class="ribbon" viewBox="0 0 985 300" aria-hidden="true">
    <polygon points="690,20 940,40 930,80 700,80" fill="var(--teal-dark)"/>
    <polygon points="405,75 965,68 965,205 405,212" fill="var(--teal)"/>
    <polygon points="555,270 620,270 600,300" fill="var(--teal-dark)"/>
  </svg>
  <div class="ribbon-text">WE OFFER COMFORTABLE<br>AND AFFORDABLE</div>
  <div class="ribbon-care">DENTAL CARE</div>

  <div class="photo" role="img" aria-label="Photo of a smiling family of four relaxing together on a white bed"></div>

  <div class="web-band">www.crestlinedentalmarbury.com.au</div>

  <div class="slogan-band">Going to the Dentist Can Be Fun!<br><span class="strong">We Put Smile In Your Life.</span></div>

  <section class="hours">
    <div class="hours-title">VISIT OUR OFFICE</div>
    <div class="hours-row"><div class="hours-day">MONDAY</div><div class="hours-time">8:30AM - 5:30PM</div></div>
    <div class="hours-row"><div class="hours-day">TUESDAY</div><div class="hours-time">12:00PM - 8:00PM</div></div>
    <div class="hours-row"><div class="hours-day small">WEDNESDAY-FRIDAY</div><div class="hours-time">8:30AM - 5:30PM</div></div>
    <div class="hours-row"><div class="hours-day">SATURDAY</div><div class="hours-time">9:00AM - 4:00PM</div></div>
  </section>

  <p class="funds">“We accept<br>all health<br>funds.”</p>

  <div class="badge">
    <svg width="210" height="210" viewBox="0 0 210 210" aria-hidden="true">
      <g fill="var(--lime)" transform="translate(105 105)">
        <rect x="-72" y="-72" width="144" height="144"/>
        <rect x="-72" y="-72" width="144" height="144" transform="rotate(15)"/>
        <rect x="-72" y="-72" width="144" height="144" transform="rotate(30)"/>
        <rect x="-72" y="-72" width="144" height="144" transform="rotate(45)"/>
        <rect x="-72" y="-72" width="144" height="144" transform="rotate(60)"/>
        <rect x="-72" y="-72" width="144" height="144" transform="rotate(75)"/>
      </g>
      <circle cx="105" cy="105" r="84" fill="var(--white)"/>
      <circle cx="105" cy="105" r="76" fill="none" stroke="var(--lime)" stroke-width="3"/>
    </svg>
    <div class="badge-text">
      <div class="badge-stars" style="top:40px">★★★</div>
      <div class="badge-pct">10%</div>
      <div class="badge-off">OFF</div>
      <div class="badge-stars" style="top:160px">★★★</div>
    </div>
  </div>

  <div class="offer-strip">10% off on all major dental. Includes fillings,<br>crowns, bridges and root canal treatment.</div>

  <div class="call-band">CALL (02) 5550 1847</div>

</main>
</body>
</html>
```